Hip and quirky Indian restaurant Menu

We need a build your own bowl/meal/wrap menu similar to Marwenda others. We would like illustrations if possible of India/veggies/chicken/animals/themes. Please utilize the colors that match the schema of the logos provided. We have included pictures you may use them if you would like to. Menu provided is our old menu.

Target Market(s)

Millenials, Ge

Industry/Entity Type

Retail

Font styles to use
Sans Serif
Decorative

Requirements
Must have
• logical placements for build your own meal options
Nice to have
• Illustrations.

```html
<!DOCTYPE html>
<html lang="en">
<head>
<meta charset="utf-8">
<title>Saffron Spoon – Menu</title>
<link rel="stylesheet" href="https://fonts.googleapis.com/css2?family=Bebas+Neue&family=Montserrat:wght@500;700&family=Raleway:wght@500&display=swap">
<style>
  :root {
    --orange: #ee643f;
    --navy: #25235f;
    --plum: #9e2160;
    --white: #ffffff;
    --peach: #fde0b8;
    --brand-navy: #2a2867;
    --wood-light: #a87a58;
    --wood-dark: #6e4a32;
  }
  * { margin: 0; padding: 0; box-sizing: border-box; }
  html, body { width: 1200px; height: 849px; overflow: hidden; background: var(--white); }
  .menu { position: relative; width: 1200px; height: 849px; background: var(--white); }

  .panel { position: absolute; color: var(--white); }
  .panel > * { position: absolute; }

  .display { font-family: "Bebas Neue", sans-serif; font-weight: 400; letter-spacing: 0.5px; }
  .body-sans { font-family: "Montserrat", sans-serif; font-weight: 500; }
  .body-light { font-family: "Raleway", sans-serif; font-weight: 500; }

  /* Brand */
  .brand { position: absolute; left: 70px; top: 40px; width: 270px; height: 200px; }
  .brand-mark { position: absolute; left: 0; top: 66px; width: 56px; height: 56px; border-radius: 50%; background: var(--peach); }
  .brand-name { position: absolute; left: 70px; top: 38px; font-family: "Bebas Neue", sans-serif; font-size: 58px; line-height: 54px; color: var(--brand-navy); }

  /* Build your own meal */
  .build { left: 30px; top: 276px; width: 375px; height: 573px; background: var(--orange); text-align: center; }
  .build > * { left: 0; width: 375px; }
  .build-title { top: 28px; font-size: 60px; line-height: 50px; }
  .build-price { top: 142px; font-size: 20px; line-height: 20px; }
  .step-title { font-family: "Montserrat", sans-serif; font-weight: 700; font-size: 15.5px; line-height: 18px; }
  .step-options { font-size: 12px; line-height: 15.4px; }

  /* Lassi / snacks */
  .drinks-snacks { left: 414px; top: 0; width: 375px; height: 586px; background: var(--navy); }
  .section-title { font-size: 34px; line-height: 31px; }
  .price-table { left: 47px; width: 310px; font-size: 12px; line-height: 15.3px; }
  .price-row { display: flex; }
  .price-row .item { width: 203px; }
  .price-row .small { width: 52px; }
  .size-head { font-family: "Montserrat", sans-serif; font-weight: 700; font-size: 7px; }
  .dish-copy { left: 47px; width: 305px; font-size: 12px; line-height: 15.3px; }
  .snack-row { display: flex; justify-content: space-between; width: 269px; }

  /* Meals */
  .meals { left: 798px; top: 382px; width: 375px; height: 467px; background: var(--plum); }
  .meals .section-title { left: 58px; }
  .meal-list { left: 57px; font-size: 12px; line-height: 15.3px; }

  /* Photo areas */
  .photo { position: absolute; }
  .photo-dishes { left: 812px; top: 36px; width: 348px; height: 334px; border-radius: 4px;
    background: linear-gradient(150deg, var(--wood-light), var(--wood-dark)); }
  .photo-puffs { left: 414px; top: 611px; width: 375px; height: 238px;
    background: linear-gradient(160deg, var(--wood-light), var(--wood-dark)); }
</style>
</head>
<body>
<div class="menu">

  <div class="brand">
    <div class="brand-mark"></div>
    <div class="brand-name">Saffron<br>Spoon</div>
  </div>

  <section class="panel build">
    <h1 class="display build-title">Build your<br>own meal</h1>
    <p class="display build-price">$8.00</p>

    <h2 class="step-title" style="top:198px">PICK BOWL/WRAP</h2>
    <p class="body-light step-options" style="top:227px">Salad Bowl, Basmati Rice Bowl,<br>Curry Rice Bowl, Paratha Wrap</p>

    <h2 class="step-title" style="top:290px">PICK MAIN CURRY OPTION</h2>
    <p class="body-light step-options" style="top:315px">Veg Korma, Chana Masala, CTM,<br>Chili Chicken, Tandoori Chicken,<br>Beef Curry +$1, Goat Curry $2</p>

    <h2 class="step-title" style="top:381px">PICK TOPPINGS</h2>
    <p class="body-light step-options" style="top:404px">Beets Thoran, Green Beans Thoran,<br>Cabbage Thoran, Chick Pea Salad<br>Cucumber Salad, diced Onion</p>

    <h2 class="step-title" style="top:472px">PICK SAUCES</h2>
    <p class="body-light step-options" style="top:496px">Original Mint, Sweet Tamarind,<br>Cool Yogurt, Mango Chilli, Tikka Masala</p>
  </section>

  <section class="panel drinks-snacks">
    <h2 class="display section-title" style="left:47px; top:60px">Lassi/<br>Indian Shakes</h2>

    <div class="price-table body-sans" style="top:117px">
      <div class="price-row size-head"><span class="item"></span><span class="small">SMALL</span><span>LARGE</span></div>
    </div>
    <div class="price-table body-sans" style="top:132px">
      <div class="price-row"><span class="item">Original Lassi</span><span class="small">2.00</span><span>2.50</span></div>
      <div class="price-row"><span class="item">Mango Lassi</span><span class="small">2.5</span><span>3.00</span></div>
      <div class="price-row"><span class="item">Rose Lassi</span><span class="small">2.5</span><span>3.00</span></div>
      <div class="price-row"><span class="item">Chai Spice Lassi</span><span class="small">2.75</span><span>3.25</span></div>
      <div class="price-row"><span class="item">Cookies N Cream Lassi</span><span class="small">2.75</span><span>3.25</span></div>
      <div class="price-row"><span class="item">Chocolate Hazelnut Lassi</span><span class="small">2.75</span><span>3.25</span></div>
    </div>

    <h2 class="display section-title" style="left:47px; top:266px">Chicken<br>Biriyani Bowl</h2>
    <p class="body-sans dish-copy" style="top:336px">The Original Indian Rice Bowl! Chicken and rice which has been baked to perfection.” Served with yogurt sauce, pickle and pappadom.</p>

    <h2 class="display section-title" style="left:47px; top:423px">Snacks</h2>
    <div class="price-table body-sans" style="top:463px">
      <div class="snack-row"><span>Samosa</span><span>$1.00</span></div>
      <div class="snack-row"><span>Veg Puffs</span><span>$1.49</span></div>
      <div class="snack-row"><span>Egg Puffs</span><span>$2.49</span></div>
      <div class="snack-row"><span>Sweet Puffs</span><span>$1.49</span></div>
      <div class="snack-row"><span>Beef Puffs</span><span>$1.49</span></div>
      <div class="snack-row"><span>Chicken Puffs</span><span>$1.49</span></div>
    </div>
  </section>

  <div class="photo photo-dishes" role="img" aria-label="Photo collage of curry bowls, biriyani and side dishes"></div>
  <div class="photo photo-puffs" role="img" aria-label="Photo of two golden puff pastries on a plate"></div>

  <section class="panel meals">
    <h2 class="display section-title" style="top:40px">Chicken<br>Meals</h2>
    <div class="body-sans meal-list" style="top:111px">
      <p>Tandoori Chicken /Fries $7</p>
      <p>Chicken Tender/ Fries $7</p>
      <p>Spicy Chicken Tender/ Fries $7</p>
    </div>

    <h2 class="display section-title" style="top:176px">Loaded<br>Fries</h2>
    <div class="body-sans meal-list" style="top:246px">
      <p>Chicken Tikka Fries</p>
      <p>Tandoori Fries</p>
      <p>Chili Chicken Fries</p>
    </div>

    <h2 class="display section-title" style="top:306px">Drinks</h2>
    <div class="body-sans meal-list" style="top:343px">
      <p>Iced Tea 32oz</p>
      <p>Lemonade 32oz</p>
      <p>Masala Tea</p>
      <p>Indian Coffee</p>
      <p>Soda Can</p>
      <p>Water Bottle</p>
    </div>
  </section>

</div>
</body>
</html>
```